Birch Spire Kilo Marsh website

we need a website to cater to 2 aspect of the business. We have Birch spire residence and birch spire office. For the office, we will get their inquire and arrange a face to face meetup to show them the office area for rent. For the residence side, it will need to be like stayrio or velupa.com. we want to allow them to book online for the date they need. We have a total of 10 different room configurations starting at $70 per night and up depending on the size of the room. example of the design is https://lumbrahaven.com/

Target Market(s)

the website should have detail information on the layout, designs, and luxury of the building.

Industry/Entity Type

office and service appartment rental/lease

Coding

Coded - Design and coding required

Number of Pages Required

5+ page

Requirements
Must have
• a luxury perspective
Nice to have
• example https://lumbrahaven.com/

```html
<!DOCTYPE html>
<html lang="en">
<head>
<meta charset="utf-8">
<title>Birch Spire Kilo Marsh</title>
<link rel="stylesheet" href="https://fonts.googleapis.com/css2?family=Noto+Sans:wght@400;600;700&display=swap">
<style>
:root{
  --ink:#1b1b1b;
  --muted:#555;
  --accent:#b08b77;
  --accent-dark:#8f6e5c;
  --sand:#e8ddd6;
  --line:#c9c9c9;
  --white:#fff;
}
*{box-sizing:border-box;margin:0;padding:0}
html,body{width:1200px;height:2787px;overflow:hidden}
body{position:relative;background:var(--white);color:var(--ink);font-family:"Noto Sans",Tahoma,sans-serif}
.abs{position:absolute}
.btn{position:absolute;background:var(--accent);color:var(--white);font-size:12px;font-weight:700;border-radius:4px;display:flex;align-items:center;justify-content:center}

/* header */
.site-header{left:0;top:0;width:1200px;height:87px;background:var(--white)}
.brand{left:57px;top:14px;width:100px;text-align:center}
.brand-mark{width:22px;height:22px;border:2px solid var(--accent);margin:0 auto 6px}
.brand-name{font-size:11px;color:var(--accent-dark);letter-spacing:.5px;white-space:nowrap}
.main-nav{left:380px;top:38px;font-size:13px}
.main-nav span{position:absolute;white-space:nowrap}
.nav-active{border-bottom:2px solid var(--accent);padding-bottom:5px}
.book-now{left:1034px;top:31px;width:109px;height:30px}

/* hero */
.hero{left:0;top:87px;width:1200px;height:528px;background:linear-gradient(180deg,#6d7784 0%,#8c8b86 40%,#9a8676 70%,#7a6656 100%)}
.hero-title{left:0;top:222px;width:1200px;text-align:center;color:var(--white);font-size:43px;font-weight:700;line-height:50px;text-shadow:0 2px 6px rgba(0,0,0,.45)}
.search-box{left:235px;top:353px;width:729px;height:98px;background:var(--white);border-radius:8px}
.field-label{position:absolute;top:26px;font-size:11px}
.field{position:absolute;top:44px;width:162px;height:30px;border:1px solid var(--line);border-radius:3px;font-size:10px;color:#888;padding:8px 16px}
.caret{position:absolute;right:10px;top:12px;width:0;height:0;border-left:4px solid transparent;border-right:4px solid transparent;border-top:5px solid #777}
.search-btn{left:572px;top:44px;width:120px;height:30px;font-size:11px;gap:6px}

/* about */
.photo{position:absolute}
.about-copy{left:583px;top:710px;width:520px;display:flex;flex-direction:column;align-items:flex-start}
.about-title{font-size:32px;font-weight:700;line-height:44px}
.about-text{margin-top:6px;width:510px;font-size:14px;line-height:20px;letter-spacing:-.2px}
.about-copy .read-more{position:static;margin-top:14px;width:108px;height:29px}

/* rooms */
.center-title{left:0;width:1200px;text-align:center;font-size:32px;font-weight:700}
.center-sub{left:0;width:1200px;text-align:center;font-size:16px;line-height:21px}
.room-card{position:absolute;width:183px;height:166px;color:var(--white);text-align:center;text-shadow:0 1px 4px rgba(0,0,0,.8);padding-top:56px}
.room-card b{display:block;font-size:28px;line-height:30px}
.room-card span{display:block;font-size:16px;line-height:20px}

/* contact */
.contact-photo{left:0;top:1620px;width:600px;height:372px;background:linear-gradient(135deg,#cfc8c0 0%,#e9e6e2 45%,#3b7f8c 80%,#b59a80 100%)}
.contact-panel{left:600px;top:1620px;width:600px;height:372px;background:var(--sand)}
.contact-title{left:652px;top:1638px;font-size:32px;font-weight:700}
.contact-text{left:653px;top:1680px;width:470px;font-size:13px;line-height:16px}
.small-label{position:absolute;font-size:10px}
.input{position:absolute;background:var(--white);border:1px solid #c8beb7;border-radius:3px;font-size:10px;color:#888;padding:9px 16px}
.send{left:1009px;top:1939px;width:109px;height:29px}

/* reviews */
.review{position:absolute;top:2194px;width:299px;height:185px;border:1px solid #ddd;box-shadow:0 2px 4px rgba(0,0,0,.2);padding:30px 30px;font-size:13px;line-height:16px}
.review h3{font-size:15px;font-weight:700;line-height:18px}
.review p{margin-top:16px}

/* footer */
.rule{height:1px;background:#555}
.footer-brand{left:82px;top:2516px;width:256px;text-align:center}
.footer-brand .brand-mark{width:60px;height:60px;margin-bottom:34px}
.footer-brand .brand-name{font-size:21px;letter-spacing:.5px}
.footer-name{left:400px;top:2519px;font-size:20px;font-weight:700}
.footer-address{left:401px;top:2552px;font-size:16px}
.icon{position:absolute;top:2596px}
.menu-title{left:832px;top:2521px;font-size:16px;font-weight:700}
.menu-link{position:absolute;font-size:16px}
.copyright{left:0;top:2741px;width:1200px;text-align:center;font-size:16px}
</style>
</head>
<body>

<header class="site-header abs">
  <div class="brand abs">
    <div class="brand-mark"></div>
    <div class="brand-name">Birch Spire Kilo Marsh</div>
  </div>
  <nav class="main-nav abs">
    <span class="nav-active" style="left:14px">Home</span>
    <span style="left:105px">Design</span>
    <span style="left:187px">Location</span>
    <span style="left:279px">Experience</span>
    <span style="left:385px">About Us</span>
  </nav>
  <div class="btn book-now">Book Now !</div>
</header>

<section class="hero abs" role="img" aria-label="Bright apartment living room with floor-to-ceiling windows overlooking the city"></section>
<h1 class="hero-title abs">Experience the Height of Luxury at Birch Spire<br>Residence. Book Your Stay Online Now!</h1>

<form class="search-box abs">
  <span class="field-label" style="left:37px">Room type</span>
  <div class="field" style="left:37px">Pick Room Type<i class="caret"></i></div>
  <span class="field-label" style="left:216px">Room Size</span>
  <div class="field" style="left:216px">Pick Room Size<i class="caret"></i></div>
  <span class="field-label" style="left:394px">Date</span>
  <div class="field" style="left:394px">Pick Date
    <svg style="position:absolute;right:9px;top:6px" width="16" height="16" viewBox="0 0 16 16" fill="none" stroke="#888"><rect x="1.5" y="2.5" width="13" height="12" rx="1"/><path d="M1.5 6h13M5 1v3M11 1v3M4 8.5h2M7 8.5h2M10 8.5h2M4 11.5h2M7 11.5h2M10 11.5h2"/></svg>
  </div>
  <div class="btn search-btn">
    <svg width="14" height="14" viewBox="0 0 14 14" fill="none" stroke="#fff" stroke-width="1.6"><circle cx="6" cy="6" r="4.5"/><path d="M9.5 9.5L13 13"/></svg>
    Search Room
  </div>
</form>

<section>
  <div class="photo" style="left:95px;top:686px;width:207px;height:145px;background:linear-gradient(180deg,#3b3f6e,#4a3a30)" role="img" aria-label="Lounge with ornate lit ceiling and dark sofas"></div>
  <div class="photo" style="left:95px;top:847px;width:207px;height:145px;background:linear-gradient(135deg,#e4e4e2,#8e9aa3)" role="img" aria-label="White living area beside tall glass windows"></div>
  <div class="photo" style="left:327px;top:686px;width:203px;height:306px;background:linear-gradient(180deg,#5e5e5c 0%,#9aa8b2 45%,#4a3b30 100%)" role="img" aria-label="Reading chair and pendant lamp facing a city view"></div>
  <div class="about-copy abs">
    <h2 class="about-title">Luxury Accomodation for staying</h2>
    <p class="about-text">Lorem ipsum dolor sit amet, consectetur adipiscing elit, sed do eiusmod tempor incididunt ut labore et dolore magna aliqua. Ut enim ad minim veniam, quis nostrud exercitation ullamco laboris nisi ut aliquip ex ea commodo consequat. Duis aute irure dolor in reprehenderit in voluptate velit esse cillum dolore eu fugiat nulla pariatur. tempor incididunt ut labore et dolore magna aliqua. Ut enim ad minim veniam, quis nostrud exercitation ullamco laboris nisi ut aliquip</p>
    <div class="btn read-more">Read More</div>
  </div>
</section>

<section>
  <h2 class="center-title abs" style="top:1071px">10 Different Room Configurations</h2>
  <p class="center-sub abs" style="top:1115px">We have a total of 10 different room configurations starting at $70 per night<br>and up depending on the size of the room</p>

  <div class="room-card" style="left:92px;top:1188px;background:linear-gradient(160deg,#2b2f6a,#6a5a4c)" role="img" aria-label="Type C one bed room"><b>Type C</b><span>One Bed Room<br>(47.00)</span></div>
  <div class="room-card" style="left:307px;top:1188px;background:linear-gradient(160deg,#8a8a88,#5e544c)" role="img" aria-label="Type A studio"><b>Type A</b><span>Studio (36.80)</span></div>
  <div class="room-card" style="left:522px;top:1188px;background:linear-gradient(160deg,#b8b6b0,#6d6258)" role="img" aria-label="Type B studio"><b>Type B</b><span>Studio (38.75)</span></div>
  <div class="room-card" style="left:737px;top:1188px;background:linear-gradient(160deg,#6c6a66,#2f3d5e)" role="img" aria-label="Type A two bed room"><b>Type A</b><span>Two Bed Room</span></div>
  <div class="room-card" style="left:952px;top:1188px;background:linear-gradient(160deg,#c7cdd2,#4e8c8a)" role="img" aria-label="Type B studio"><b>Type B</b><span>Studiio (39.55)</span></div>

  <div class="room-card" style="left:92px;top:1377px;background:linear-gradient(160deg,#c7cdd2,#4e8c8a)" role="img" aria-label="Type B studio"><b>Type B</b><span>Studiio (39.55)</span></div>
  <div class="room-card" style="left:307px;top:1377px;background:linear-gradient(160deg,#6c6a66,#2f3d5e)" role="img" aria-label="Type A two bed room"><b>Type A</b><span>Two Bed Room</span></div>
  <div class="room-card" style="left:522px;top:1375px;background:linear-gradient(160deg,#2b2f6a,#6a5a4c)" role="img" aria-label="Type C one bed room"><b>Type C</b><span>One Bed Room<br>(47.00)</span></div>
  <div class="room-card" style="left:737px;top:1375px;background:linear-gradient(160deg,#8a8a88,#5e544c)" role="img" aria-label="Type A studio"><b>Type A</b><span>Studio (36.80)</span></div>
  <div class="room-card" style="left:952px;top:1375px;background:linear-gradient(160deg,#b8b6b0,#6d6258)" role="img" aria-label="Type B studio"><b>Type B</b><span>Studio (38.75)</span></div>
</section>

<section>
  <div class="contact-photo abs" role="img" aria-label="Family relaxing together on a large white bed"></div>
  <div class="contact-panel abs"></div>
  <h2 class="contact-title abs">Reach Us</h2>
  <p class="contact-text abs">For any inquiries or to schedule a viewing, please fill out the form below. We look forward to assisting you in any way we can.</p>
  <span class="small-label" style="left:653px;top:1730px">Full Name</span>
  <div class="input" style="left:653px;top:1747px;width:225px;height:29px">Your Name</div>
  <span class="small-label" style="left:893px;top:1730px">Email</span>
  <div class="input" style="left:893px;top:1747px;width:225px;height:29px">Your Email</div>
  <span class="small-label" style="left:653px;top:1790px">Mesage</span>
  <div class="input" style="left:653px;top:1807px;width:465px;height:118px">Your Message</div>
  <div class="btn send">Send</div>
</section>

<section>
  <h2 class="center-title abs" style="top:2074px">Overheard From Visitors</h2>
  <p class="center-sub abs" style="top:2123px">Experience luxury at its finest—our exquisite amenities, flawless service, and opulent<br>ambiance have garnered glowing reviews from our discerning guests</p>
  <article class="review" style="left:102px">
    <h3>Mirela Hartwell</h3>Type C - One Bed Room
    <p>My stay at Birch Spire Kilo Marsh was simply sublime. The sleek, modern design combined with the breathtaking views made for an unforgettable experience. I can't wait to return!</p>
  </article>
  <article class="review" style="left:438px">
    <h3>Daniel Osei</h3>Type C - Two Bed Room
    <p>Birch Spire Kilo Marsh is a true gem in the heart of the city. The luxurious amenities and attention to detail are second to none. A perfect blend of comfort and sophistication</p>
  </article>
  <article class="review" style="left:775px">
    <h3>Priya Lindqvist</h3>Type C - One Bed Room
    <p>Staying at Birch Spire Kilo Marsh was a delight from start to finish. The elegant decor, spacious rooms, and panoramic views made me feel like royalty.</p>
  </article>
</section>

<footer>
  <div class="rule abs" style="left:93px;top:2472px;width:1014px"></div>
  <div class="footer-brand abs">
    <div class="brand-mark"></div>
    <div class="brand-name">Birch Spire Kilo Marsh</div>
  </div>
  <div class="footer-name abs">Birch Spire Kilo Marsh</div>
  <div class="footer-address abs">88 Larkfield Row Ashbury, OR 97310</div>
  <svg class="icon" style="left:403px" width="34" height="34" viewBox="0 0 24 24" fill="var(--accent)"><path d="M6.6 10.8c1.4 2.8 3.8 5.1 6.6 6.6l2.2-2.2c.3-.3.7-.4 1-.2 1.1.4 2.3.6 3.6.6.6 0 1 .4 1 1V20c0 .6-.4 1-1 1C10.6 21 3 13.4 3 4c0-.6.4-1 1-1h3.5c.6 0 1 .4 1 1 0 1.3.2 2.5.6 3.6.1.3 0 .7-.2 1z"/></svg>
  <svg class="icon" style="left:468px;top:2598px" width="40" height="32" viewBox="0 0 24 19"><rect x="1" y="1" width="22" height="17" rx="2" fill="var(--accent)"/><path d="M2 3l10 7 10-7" fill="none" stroke="#fff" stroke-width="2"/></svg>
  <svg class="icon" style="left:538px" width="34" height="34" viewBox="0 0 34 34"><circle cx="17" cy="17" r="16" fill="var(--accent)"/></svg>
  <svg class="icon" style="left:601px" width="34" height="34" viewBox="0 0 34 34"><circle cx="17" cy="17" r="16" fill="var(--accent)"/></svg>

  <div class="menu-title abs">Menu</div>
  <span class="menu-link" style="left:832px;top:2552px">Home</span>
  <span class="menu-link" style="left:918px;top:2552px">Experiences</span>
  <span class="menu-link" style="left:832px;top:2589px">Design</span>
  <span class="menu-link" style="left:918px;top:2589px">About Us</span>
  <span class="menu-link" style="left:832px;top:2626px">Location</span>

  <div class="rule abs" style="left:97px;top:2717px;width:1015px"></div>
  <div class="copyright abs">© Copyright Birch Spire Kilo Marsh 2024 | All Right Reserved</div>
</footer>

</body>
</html>
```